Banners for Website and Social Media

Technology Consulting and Services company requires several banners that integrate our logo that can be used on a basic website that we are designing. The design will also be used on social media platforms. Require a variety of sizes and shapes to be included. Need at least two variations for a website header, more variations will put you at the top of the leaderboard.

Target Market(s)

Non-Profit Mental Health Agencies, small business

Font styles to use
Serif

Requirements
Must have
• Show the idea of connecting with our clients. We require the following approximate sizes, they do not have to be exact:

2 x variations 1080px x 600px for website header
1 x 1128px x 191px for Brindlepost
1 x 590px x 175px for Email Marketing
1 x 300px x 250px for Advertising

Colours should compliment the logo that has been provided.
Nice to have
• Could integrate key words and phrases in the graphic but not standout as a tagline or title.

- Engaged
- Ethical Technology
- Support
- Connected
Should not have
• Banner should avoid having people in it. Prefer a more abstract feel.

```html
<!DOCTYPE html>
<html lang="en">
<head>
<meta charset="utf-8">
<title>Veranta Technology — Banner Set</title>
<link rel="stylesheet" href="https://fonts.googleapis.com/css2?family=Audiowide&family=Open+Sans:wght@700&display=swap">
<style>
  :root {
    --page-bg: #ebebeb;
    --brand-blue: #1c4a90;
    --network-cyan: #2fd9ef;
    --accent-orange: #f7a031;
    --white: #ffffff;
  }
  * { margin: 0; padding: 0; box-sizing: border-box; }
  html, body { width: 900px; height: 1200px; overflow: hidden; background: var(--page-bg); }
  .canvas { position: relative; width: 900px; height: 1200px; }

  .banner { position: absolute; background: var(--white); overflow: hidden; }
  .banner svg.backdrop { position: absolute; inset: 0; display: block; }

  .keyword {
    position: absolute;
    font-family: "Audiowide", sans-serif;
    color: var(--white);
    letter-spacing: 0.08em;
    white-space: nowrap;
    line-height: 1;
    transform: translateY(-50%);
  }
  .keyword::before {
    content: "";
    position: absolute;
    top: 50%;
    transform: translateY(-50%);
    background: var(--accent-orange);
    clip-path: polygon(0 0, 100% 50%, 0 100%);
  }

  .brand-name {
    position: absolute;
    font-family: "Audiowide", sans-serif;
    color: var(--brand-blue);
    white-space: nowrap;
    line-height: 1;
    transform: translate(-50%, -50%);
  }

  .set-label {
    position: absolute;
    left: 14px;
    font-family: "Open Sans", sans-serif;
    font-weight: 700;
    font-size: 16px;
    letter-spacing: 0.12em;
    color: var(--brand-blue);
    transform: translateY(-50%);
  }

  /* website header */
  .banner--website { left: 126px; top: 0; width: 648px; height: 360px; }
  .banner--website .keyword { left: 225px; font-size: 13.8px; }
  .banner--website .keyword::before { left: -25px; width: 17px; height: 12px; }
  .banner--website .brand-name { left: 324px; top: 333px; font-size: 13.3px; }

  /* brindlepost header */
  .banner--brindlepost { left: 112px; top: 508px; width: 677px; height: 115px; }
  .banner--brindlepost .keyword { font-size: 11.6px; }
  .banner--brindlepost .keyword::before { left: -21px; width: 14px; height: 10px; }
  .banner--brindlepost .brand-name { left: 594px; top: 92px; font-size: 10.3px; }

  /* email marketing */
  .banner--email { left: 273px; top: 762px; width: 354px; height: 105px; }
  .banner--email .keyword { font-size: 7.8px; }
  .banner--email .keyword::before { left: -18px; width: 12px; height: 8px; }
  .banner--email .brand-name { left: 289px; top: 89px; font-size: 7.4px; }

  /* advertising */
  .banner--ad { left: 360px; top: 984px; width: 180px; height: 150px; }
  .banner--ad .keyword { font-size: 5.3px; }
  .banner--ad .keyword::before { left: -10px; width: 7px; height: 5px; }
  .banner--ad .brand-name { left: 90px; top: 136px; font-size: 6.6px; }
</style>
</head>
<body>
<main class="canvas">

  <!-- Website header -->
  <section class="banner banner--website">
    <svg class="backdrop" width="648" height="360" viewBox="0 0 648 360">
      <defs>
        <radialGradient id="web-network" cx="0.28" cy="0.55" r="0.6">
          <stop offset="0" stop-color="#2fd9ef" stop-opacity="0.55"/>
          <stop offset="0.5" stop-color="#2a7fd8" stop-opacity="0.35"/>
          <stop offset="1" stop-color="#1c4a90" stop-opacity="0"/>
        </radialGradient>
      </defs>
      <polygon points="0,0 648,0 648,269 0,298" fill="#1c4a90"/>
      <g role="img" aria-label="Abstract network of connected nodes and lines in cyan and blue">
        <polygon points="0,0 420,0 420,279 0,298" fill="url(#web-network)"/>
      </g>
      <circle cx="323" cy="280" r="49" fill="#ffffff"/>
    </svg>
    <span class="keyword" style="top:74px">ENGAGED</span>
    <span class="keyword" style="top:118px">SUPPORT</span>
    <span class="keyword" style="top:163px">CONNECTED</span>
    <span class="keyword" style="top:208px">ETHICAL&nbsp; TECHNOLOGY</span>
    <span class="brand-name">VERANTA TECHNOLOGY</span>
  </section>
  <h2 class="set-label" style="top:383px">WEBSITE HEADER</h2>

  <!-- Brindlepost header -->
  <section class="banner banner--brindlepost">
    <svg class="backdrop" width="677" height="115" viewBox="0 0 677 115">
      <defs>
        <radialGradient id="bp-network" cx="0.35" cy="0.5" r="0.65">
          <stop offset="0" stop-color="#2fd9ef" stop-opacity="0.5"/>
          <stop offset="0.55" stop-color="#2a7fd8" stop-opacity="0.3"/>
          <stop offset="1" stop-color="#1c4a90" stop-opacity="0"/>
        </radialGradient>
      </defs>
      <polygon points="0,0 677,0 677,67 0,115" fill="#1c4a90"/>
      <g role="img" aria-label="Abstract network of connected nodes and lines in cyan and blue">
        <polygon points="0,0 280,0 280,95 0,115" fill="url(#bp-network)"/>
      </g>
      <circle cx="594" cy="53" r="38" fill="#ffffff"/>
    </svg>
    <span class="keyword" style="left:174px; top:28px">ENGAGED</span>
    <span class="keyword" style="left:174px; top:56px">SUPPORT</span>
    <span class="keyword" style="left:305px; top:28px">CONNECTED</span>
    <span class="keyword" style="left:305px; top:56px">ETHICAL&nbsp; TECHNOLOGY</span>
    <span class="brand-name">VERANTA TECHNOLOGY</span>
  </section>
  <h2 class="set-label" style="top:646px">BRINDLEPOST HEADER</h2>

  <!-- Email marketing -->
  <section class="banner banner--email">
    <svg class="backdrop" width="354" height="105" viewBox="0 0 354 105">
      <defs>
        <radialGradient id="em-network" cx="0.2" cy="0.3" r="0.7">
          <stop offset="0" stop-color="#2a7fd8" stop-opacity="0.45"/>
          <stop offset="1" stop-color="#1c4a90" stop-opacity="0"/>
        </radialGradient>
      </defs>
      <polygon points="0,0 354,0 354,64 0,96" fill="#1c4a90"/>
      <g role="img" aria-label="Abstract network of connected nodes and lines in blue">
        <polygon points="0,0 200,0 200,78 0,96" fill="url(#em-network)"/>
      </g>
      <circle cx="289" cy="60" r="28" fill="#ffffff"/>
    </svg>
    <span class="keyword" style="left:25px; top:24px">ENGAGED</span>
    <span class="keyword" style="left:25px; top:52px">SUPPORT</span>
    <span class="keyword" style="left:126px; top:24px">CONNECTED</span>
    <span class="keyword" style="left:126px; top:52px">ETHICAL&nbsp; TECHNOLOGY</span>
    <span class="brand-name">VERANTA TECHNOLOGY</span>
  </section>
  <h2 class="set-label" style="top:886px">EMAIL MARKETING</h2>

  <!-- Advertising -->
  <section class="banner banner--ad">
    <svg class="backdrop" width="180" height="150" viewBox="0 0 180 150">
      <defs>
        <radialGradient id="ad-network" cx="0.15" cy="0.55" r="0.75">
          <stop offset="0" stop-color="#2fd9ef" stop-opacity="0.5"/>
          <stop offset="0.6" stop-color="#2a7fd8" stop-opacity="0.25"/>
          <stop offset="1" stop-color="#1c4a90" stop-opacity="0"/>
        </radialGradient>
      </defs>
      <polygon points="0,0 180,0 180,115 0,122" fill="#1c4a90"/>
      <g role="img" aria-label="Abstract network of connected nodes and lines in cyan and blue">
        <polygon points="0,0 110,0 110,118 0,122" fill="url(#ad-network)"/>
      </g>
      <circle cx="90" cy="109" r="24" fill="#ffffff"/>
    </svg>
    <span class="keyword" style="left:18px; top:37px">ENGAGED</span>
    <span class="keyword" style="left:18px; top:55px">SUPPORT</span>
    <span class="keyword" style="left:85px; top:37px">CONNECTED</span>
    <span class="keyword" style="left:85px; top:55px">ETHICAL&nbsp; TECHNOLOGY</span>
    <span class="brand-name">VERANTA TECHNOLOGY</span>
  </section>
  <h2 class="set-label" style="top:1148px">ADVERTISING</h2>

</main>
</body>
</html>
```